Dog themed post card for homeowners that may be willing to sell their house.

We will be sending these postcards to homeowners that may be interested in selling their house. Our business is themed around our dog "Wexley"- Wexley Buys Houses. We are using her as the focal point of the business because typically these homeowners get lots of mailers that are similar and we would like stand out with an inviting puppy dog.
We would like to included the icon for facebook and instragam with her handle "@WexleyBuysHouses" and her website WexleyBuysHouses.example and our phone number 555-814-2760.
We will be sending these postcards in batches to various subdivisions. For that reason please consider a format that can easily change the name of the subdivision. We are including the subdivision name because we want the postcard to be slightly more personal/targeted.
Our business is just starting and we would like to get some brand recognition going. We envision Wexley Buys Houses predominately displayed somehow.
I have attached numerous pictures of Wexley. We envision using one on each side of the postcard. Below are phrases we would like to include on the postcard in a format that you see fitting. Please use the verbiage below and not what is sketched on the uploaded postcard. The below verbiage is the most up to date.
-I recently bought a house in (subdivision name) and would love to buy yours.
-Call my humans today so we can give you a no obligation offer
-No money out of your pocket
-Quick closing
-Any condition
-Can help with moving expenses

Target Market(s)

Home owners with equity in their house that may need to sell quickly. These are generally people that do not enjoy the buying/selling of real estate. It can sometimes be someone who has recently inherited a home and doesnt want to deal with the headache. Other times it may be someone going through a divorce or forclosure and want to sell their home quickly.

Industry/Entity Type

Direct Marketing

Requirements
Must have
• Happy and bright feel. This industry is saturated with less than ethical people and we are trying to convey a very clean, honest, straight forward and scam-free process.

```html
<!DOCTYPE html>
<html lang="en">
<head>
<meta charset="utf-8">
<title>Wexley Buys Houses – Postcard Concepts</title>
<link href="https://fonts.googleapis.com/css2?family=Montserrat:wght@400;500;600;700;800;900&display=swap" rel="stylesheet">
<style>
  :root {
    --backdrop: #606268;
    --white: #ffffff;
    --coral: #f47b63;
    --teal: #1aa39a;
    --rust: #c8651b;
    --maroon: #8b1010;
    --slate: #555559;
    --ink: #4a4a4a;
    --rule: #b5b5b5;
  }
  * { box-sizing: border-box; margin: 0; padding: 0; }
  html, body { width: 1063px; height: 1200px; overflow: hidden; }
  body {
    background: var(--backdrop);
    font-family: "Montserrat", sans-serif;
    position: relative;
  }
  .card {
    position: absolute;
    width: 429px;
    height: 335px;
    background: var(--white);
    overflow: hidden;
  }
  .front-1 { left: 67px; top: 58px; }
  .front-2 { left: 68px; top: 427px; }
  .front-3 { left: 68px; top: 797px; }
  .back-1 { left: 565px; top: 56px; }
  .back-2 { left: 565px; top: 425px; }
  .back-3 { left: 565px; top: 797px; }

  .dog-photo {
    position: absolute; top: 0; right: 0; bottom: 0; left: 170px;
    background:
      radial-gradient(ellipse 38% 50% at 68% 58%, #b7b4bc 0%, #cdc8cb 45%, rgba(230,224,222,0) 100%),
      radial-gradient(ellipse 30% 40% at 100% 45%, #a7836c 0%, rgba(167,131,108,0) 100%),
      radial-gradient(ellipse 15% 20% at 98% 15%, #6f8f4e 0%, rgba(111,143,78,0) 100%),
      linear-gradient(to right, #ffffff 0%, #f1eceb 30%, #e5dedc 100%);
  }
  .house-photo {
    position: absolute; inset: 0;
    background:
      radial-gradient(ellipse 12% 22% at 35% 68%, #b9b9b9 0%, rgba(185,185,185,0) 100%),
      linear-gradient(to bottom, rgba(255,255,255,0) 60%, #ededed 100%),
      linear-gradient(155deg, #c4c4c4 0%, #d9d9d9 35%, #ececec 60%, #ffffff 85%);
  }

  .brand-line {
    position: absolute; left: 22px; top: 15px;
    font-size: 29px; font-weight: 700; letter-spacing: -0.3px; white-space: nowrap;
  }
  .front-1 .brand-line { color: var(--teal); }
  .front-2 .brand-line { color: var(--maroon); }
  .front-3 .brand-line { color: var(--maroon); top: 24px; }

  .thought-bubble { position: absolute; left: 0; top: 0; }
  .bubble-copy {
    position: absolute; left: 45px; top: 92px; width: 200px;
    text-align: center; color: var(--teal);
    font-size: 14.5px; font-weight: 700; line-height: 19px;
    transform: rotate(-14deg);
  }
  .blank {
    display: inline-block; width: 105px; border-bottom: 1px dotted var(--teal);
    vertical-align: 2px;
  }

  .perks { position: absolute; left: 21px; list-style: none; font-size: 11px; color: var(--ink); font-weight: 500; }
  .perks li { height: 15.5px; display: flex; align-items: center; gap: 4px; }
  .perks svg { width: 8px; height: 8px; flex: none; }
  .front-1 .perks { top: 233px; }
  .front-2 .perks { top: 261px; }

  .cta-strip {
    position: absolute; left: 0; right: 0; bottom: 0; height: 26px;
    background: var(--white);
    color: var(--teal); font-weight: 800; font-size: 12px;
    padding-left: 20px; line-height: 24px;
  }

  .headline {
    position: absolute; left: 22px; color: var(--slate);
    font-weight: 700; font-size: 19.5px; line-height: 20px;
  }
  .front-2 .headline { top: 59px; }
  .headline .blank-rule {
    display: inline-block; width: 115px; border-bottom: 1px dotted #999; vertical-align: -2px;
  }

  .offer-banner { position: absolute; left: 0; }
  .front-2 .offer-banner { top: 148px; }
  .front-3 .offer-banner { top: 214px; }
  .offer-banner .copy {
    position: absolute; left: 22px; top: 6px; color: var(--white);
    font-size: 14.5px; line-height: 14px; font-weight: 500;
  }
  .offer-banner .copy strong { display: block; font-weight: 800; margin-top: 3px; font-size: 14px; }

  .contact { position: absolute; left: 20px; display: flex; align-items: center; gap: 3px; }
  .front-2 .contact { top: 212px; }
  .front-3 .contact { top: 280px; }
  .contact .phone-number { color: var(--maroon); font-weight: 800; font-size: 21px; line-height: 21px; letter-spacing: -0.3px; }
  .contact .web { color: var(--rust); font-weight: 700; font-size: 10.5px; line-height: 12px; }

  .base-rule { position: absolute; left: 0; right: 0; bottom: 0; height: 4px; background: var(--maroon); }

  .caps-copy {
    position: absolute; left: 23px; color: var(--slate); text-transform: uppercase;
    font-weight: 500; font-size: 19.5px; line-height: 20px;
  }
  .caps-copy.top { top: 97px; }
  .caps-copy.bottom { top: 163px; }
  .area-slot {
    position: absolute; left: 23px; top: 142px; width: 206px;
    border-bottom: 1px solid var(--ink); text-align: center;
    font-size: 9.5px; color: #8d8d8d; padding-bottom: 2px; letter-spacing: 0.3px;
  }

  .stamp-box {
    position: absolute; left: 359px; top: 18px; width: 53px; height: 59px;
    border: 1px solid #9a9a9a; background: rgba(255,255,255,0.6);
  }
  .address-line { position: absolute; left: 262px; width: 147px; border-top: 1px solid var(--rule); }

  .benefit { position: absolute; width: 100px; text-align: center; }
  .benefit .badge {
    display: block; margin: 0 auto; width: 40px; height: 40px; border-radius: 50%;
    background: var(--maroon);
  }
  .benefit .badge svg { width: 40px; height: 40px; display: block; }
  .benefit p { font-size: 10.5px; line-height: 11px; color: #262626; font-weight: 500; margin-top: 3px; text-transform: uppercase; }
  .details-pill {
    position: absolute; left: 25px; top: 182px; width: 177px; height: 16px;
    border: 1px solid var(--maroon); border-radius: 9px; background: rgba(255,255,255,0.7);
    font-size: 9px; line-height: 14px; text-align: center; color: #333; font-weight: 500;
  }
  .back-3 .contact { left: 18px; top: 205px; }
  .social-handle {
    position: absolute; left: 54px; top: 243px; display: flex; align-items: center; gap: 3px;
    font-size: 10px; color: #333; font-weight: 500;
  }
  .social-handle .dot { width: 9px; height: 9px; border-radius: 50%; background: var(--maroon); }
</style>
</head>
<body>

<!-- Front: playful coral and teal -->
<section class="card front-1">
  <div class="dog-photo" role="img" aria-label="Wexley, a fluffy grey and white dog in a striped bandana, sitting on a garden path"></div>
  <h1 class="brand-line">Wexley Buys Houses</h1>
  <svg class="thought-bubble" width="429" height="335" viewBox="0 0 429 335">
    <path d="M25 170 C10 120 60 90 150 70 C230 52 250 56 268 66 C300 80 320 120 300 160 C282 190 240 198 210 205 C160 216 85 228 50 210 C35 202 28 190 25 170 Z" fill="none" stroke="var(--coral)" stroke-width="1.2"/>
    <circle cx="172" cy="199" r="10" fill="var(--white)" stroke="var(--coral)" stroke-width="1.2"/>
    <circle cx="194" cy="211" r="6" fill="var(--white)" stroke="var(--coral)" stroke-width="1.2"/>
    <circle cx="212" cy="209" r="4" fill="var(--white)" stroke="var(--coral)" stroke-width="1.2"/>
  </svg>
  <p class="bubble-copy">I recently bought a<br>house in <span class="blank"></span><br>and would love to buy<br>yours.</p>
  <ul class="perks">
    <li><svg viewBox="0 0 10 10"><circle cx="5" cy="5" r="4.3" fill="none" stroke="var(--teal)" stroke-width="1.2"/><path d="M3 5.2 L4.5 6.6 L7.2 3.6" fill="none" stroke="var(--teal)" stroke-width="1.3"/></svg>No money out of your pocket</li>
    <li><svg viewBox="0 0 10 10"><circle cx="5" cy="5" r="4.3" fill="none" stroke="var(--teal)" stroke-width="1.2"/><path d="M3 5.2 L4.5 6.6 L7.2 3.6" fill="none" stroke="var(--teal)" stroke-width="1.3"/></svg>Quick closing</li>
    <li><svg viewBox="0 0 10 10"><circle cx="5" cy="5" r="4.3" fill="none" stroke="var(--teal)" stroke-width="1.2"/><path d="M3 5.2 L4.5 6.6 L7.2 3.6" fill="none" stroke="var(--teal)" stroke-width="1.3"/></svg>Any condition</li>
    <li><svg viewBox="0 0 10 10"><circle cx="5" cy="5" r="4.3" fill="none" stroke="var(--teal)" stroke-width="1.2"/><path d="M3 5.2 L4.5 6.6 L7.2 3.6" fill="none" stroke="var(--teal)" stroke-width="1.3"/></svg>Can help with moving expenses</li>
  </ul>
  <p class="cta-strip">Call my humans today so we can give you a no obligation offer</p>
</section>

<!-- Back: blank address side -->
<section class="card back-1">
  <div class="house-photo" role="img" aria-label="Faded photo of a white house with Wexley sitting on the lawn"></div>
  <div class="stamp-box"></div>
  <div class="address-line" style="top:139px"></div>
  <div class="address-line" style="top:167px"></div>
  <div class="address-line" style="top:196px"></div>
</section>

<!-- Front: maroon and rust -->
<section class="card front-2">
  <div class="dog-photo" role="img" aria-label="Wexley, a fluffy grey and white dog in a striped bandana, sitting on a garden path"></div>
  <h1 class="brand-line">Wexley Buys Houses</h1>
  <p class="headline">I recently bought a<br>house in <span class="blank-rule"></span><br>and would love to<br>buy yours.</p>
  <div class="offer-banner">
    <svg width="240" height="82" viewBox="0 0 240 82">
      <path d="M0 0 H207 L222 57 H0 Z" fill="var(--maroon)"/>
      <path d="M202 57 H222 L202 81 Z" fill="#5e0909"/>
    </svg>
    <p class="copy">Call my humans today<br>so we can give you a<strong>NO OBLIGATION OFFER</strong></p>
  </div>
  <div class="contact">
    <svg width="32" height="32" viewBox="0 0 32 32"><rect x="9" y="2" width="16" height="28" rx="3" fill="var(--rust)"/><rect x="12" y="6" width="10" height="18" fill="var(--white)"/><path d="M4 16 Q2 24 9 28 L9 16 Z" fill="var(--rust)"/></svg>
    <div><div class="phone-number">555-814-2760</div><div class="web">WexleyBuysHouses.example</div></div>
  </div>
  <ul class="perks">
    <li><svg viewBox="0 0 10 10"><circle cx="5" cy="5" r="4.3" fill="none" stroke="var(--rust)" stroke-width="1.2"/><path d="M3 5.2 L4.5 6.6 L7.2 3.6" fill="none" stroke="var(--maroon)" stroke-width="1.3"/></svg>No money out of your pocket</li>
    <li><svg viewBox="0 0 10 10"><circle cx="5" cy="5" r="4.3" fill="none" stroke="var(--rust)" stroke-width="1.2"/><path d="M3 5.2 L4.5 6.6 L7.2 3.6" fill="none" stroke="var(--maroon)" stroke-width="1.3"/></svg>Quick closing</li>
    <li><svg viewBox="0 0 10 10"><circle cx="5" cy="5" r="4.3" fill="none" stroke="var(--rust)" stroke-width="1.2"/><path d="M3 5.2 L4.5 6.6 L7.2 3.6" fill="none" stroke="var(--maroon)" stroke-width="1.3"/></svg>Any condition</li>
    <li><svg viewBox="0 0 10 10"><circle cx="5" cy="5" r="4.3" fill="none" stroke="var(--rust)" stroke-width="1.2"/><path d="M3 5.2 L4.5 6.6 L7.2 3.6" fill="none" stroke="var(--maroon)" stroke-width="1.3"/></svg>Can help with moving expenses</li>
  </ul>
  <div class="base-rule"></div>
</section>

<section class="card back-2">
  <div class="house-photo" role="img" aria-label="Faded photo of a white house with Wexley sitting on the lawn"></div>
  <div class="stamp-box"></div>
  <div class="address-line" style="top:139px"></div>
  <div class="address-line" style="top:167px"></div>
  <div class="address-line" style="top:196px"></div>
</section>

<!-- Front: caps headline version -->
<section class="card front-3">
  <div class="dog-photo" role="img" aria-label="Wexley, a fluffy grey and white dog in a striped bandana, sitting on a garden path"></div>
  <h1 class="brand-line">Wexley Buys Houses</h1>
  <p class="caps-copy top">I recently<br>bought a house in</p>
  <p class="area-slot">WRITE AREA HERE</p>
  <p class="caps-copy bottom">and would love to<br>buy yours.</p>
  <div class="offer-banner">
    <svg width="240" height="86" viewBox="0 0 240 86">
      <path d="M0 0 H218 L233 60 H0 Z" fill="var(--maroon)"/>
      <path d="M212 60 H233 L212 86 Z" fill="#5e0909"/>
    </svg>
    <p class="copy">Call my humans today<br>so we can give you a<strong>NO OBLIGATION OFFER</strong></p>
  </div>
  <div class="contact">
    <svg width="32" height="32" viewBox="0 0 32 32"><rect x="9" y="2" width="16" height="28" rx="3" fill="var(--rust)"/><rect x="12" y="6" width="10" height="18" fill="var(--white)"/><path d="M4 16 Q2 24 9 28 L9 16 Z" fill="var(--rust)"/></svg>
    <div><div class="phone-number">555-814-2760</div><div class="web">WexleyBuysHouses.example</div></div>
  </div>
  <div class="base-rule"></div>
</section>

<!-- Back: benefits and contact -->
<section class="card back-3">
  <div class="house-photo" role="img" aria-label="Faded photo of a white house with Wexley sitting on the lawn"></div>
  <div class="stamp-box"></div>
  <div class="address-line" style="top:139px"></div>
  <div class="address-line" style="top:167px"></div>
  <div class="address-line" style="top:196px"></div>

  <div class="benefit" style="left:16px; top:17px">
    <span class="badge"><svg viewBox="0 0 40 40"><rect x="11" y="14" width="18" height="13" rx="2" fill="var(--white)"/><rect x="22" y="18" width="7" height="5" fill="var(--maroon)"/></svg></span>
    <p>No money<br>out of your<br>pocket</p>
  </div>
  <div class="benefit" style="left:110px; top:17px">
    <span class="badge"><svg viewBox="0 0 40 40"><path d="M11 20 L20 12 L29 20 V28 H11 Z" fill="var(--white)"/><rect x="17" y="22" width="6" height="6" fill="var(--maroon)"/></svg></span>
    <p>Can help<br>with moving<br>expenses</p>
  </div>
  <div class="benefit" style="left:16px; top:101px">
    <span class="badge"><svg viewBox="0 0 40 40"><path d="M13 10 H24 L28 14 V30 H13 Z" fill="var(--white)"/><path d="M20 16 V25 M16.5 21.5 L20 25 L23.5 21.5" fill="none" stroke="var(--maroon)" stroke-width="2"/></svg></span>
    <p>Quick<br>closing</p>
  </div>
  <div class="benefit" style="left:110px; top:101px">
    <span class="badge"><svg viewBox="0 0 40 40"><path d="M9 20 L16 14 L21 17 L26 14 L31 20 L22 27 Z" fill="var(--white)"/></svg></span>
    <p>Any<br>condition</p>
  </div>

  <p class="details-pill">FOR MORE DETAILS PLEASE CALL</p>
  <div class="contact">
    <svg width="32" height="32" viewBox="0 0 32 32"><rect x="9" y="2" width="16" height="28" rx="3" fill="var(--rust)"/><rect x="12" y="6" width="10" height="18" fill="var(--white)"/><path d="M4 16 Q2 24 9 28 L9 16 Z" fill="var(--rust)"/></svg>
    <div><div class="phone-number">555-814-2760</div><div class="web">WexleyBuysHouses.example</div></div>
  </div>
  <p class="social-handle"><span class="dot"></span>@WexleyBuysHouses</p>
</section>

</body>
</html>
```